www.tlorvantix.com

We are a company that is in the business of extending the life of surgical equipment by repairing or refurbishing equipment to save hospitals, surgery centers and clinics money. We call ourselves Pelbrook Medical Corporation. We are in need of a website that delivers the "feel" of what of we do everyday. A website that explains our services but at the same time has a touch that is different from the rest. Many companies repair but their websites may not "pull" customers to inquire, we need that punch. At this time we are not looking for e-commerce but would like the option of adding that in the future. We do sell new and used equipment, so we like to be able to highlight those manufacturers on our site. We would like the website to have enough layouts for pictures to describe what we repair.
Target Market(s)
Biomedical Technicians and Managers, Hospital Purchasing Departments, OR Managers, type of facilities that our customer exists in, hospitals, surgery centers, clinics, animal hospitals
Industry/Entity Type
E-Commerce
Requirements
Must have
- An easy to navigate website, modern looking.
Easy to modify with pictures and or additional web pages
The winning designer to be available for future modifications and changes
Website to be unique compared to our competition, which are numerous
Nice to have
- E-Commerce capability

```html
<!DOCTYPE html>
<html lang="en">
<head>
<meta charset="utf-8">
<title>Pelbrook Medical Corporation</title>
<link rel="stylesheet" href="https://fonts.googleapis.com/css2?family=Arimo:wght@400;700&family=Oswald:wght@500;600&family=Cinzel:wght@400&display=swap">
<style>
:root{
  --brand-blue:#1f6ea8;
  --nav-active:#5aaedc;
  --accent-orange:#d2571b;
  --soft-orange:#f0b08a;
  --ink:#151515;
  --body-grey:#6b6b6b;
  --rule-grey:#c9c9c9;
  --rule-blue:#9fd0e6;
  --icon-slate:#5d6a80;
  --title-teal:#3a8fb0;
  --banner-blue:#2d6eb0;
  --page:#ffffff;
}
*{margin:0;padding:0;box-sizing:border-box}
html,body{width:1200px;height:2352px;overflow:hidden;background:var(--page)}
body{position:relative;font-family:"Arimo",Arial,sans-serif;color:var(--ink)}
.abs{position:absolute}
.top-rule{left:0;top:41px;width:1200px;height:2px;background:#e3e3e3}
.top-tab{left:580px;top:31px;width:87px;height:10px;background:#7d8596}
.top-divider{top:0;width:1px;height:41px;background:#e3e3e3}

.logo{left:110px;top:116px}
.logo-name{font-size:31px;font-weight:700;color:var(--brand-blue);letter-spacing:.5px;line-height:1}
.logo-tag{font-size:14px;font-weight:700;color:var(--accent-orange);line-height:1.2}

.main-nav{top:134px;font-size:20px;font-weight:700;color:var(--brand-blue)}
.main-nav span{position:absolute;white-space:nowrap}
.main-nav .current{color:var(--nav-active);font-weight:400}

.hero-shadow{left:150px;top:700px;width:900px;height:70px;border-radius:50%;background:radial-gradient(ellipse at center,rgba(0,0,0,.35),rgba(0,0,0,0) 70%)}
.hero{left:132px;top:238px;width:936px;height:496px;background:linear-gradient(120deg,#3c5f86 0%,#6f8fb2 35%,#a9bdd3 55%,#5f8fb8 75%,#2d5278 100%)}

.section-rule{height:1px;background:#333}
.icon-badge{border-radius:50%;background:var(--icon-slate)}
.about-title{left:492px;top:813px;font-size:23px;font-weight:700;color:var(--accent-orange)}

.col-title{font-size:23px;font-weight:700;line-height:1.15;color:var(--ink)}
.map{left:192px;top:955px;width:120px;height:91px;border-radius:14px;background:radial-gradient(ellipse at 40% 45%,#3a3a3a,#111 70%)}
.client-list{left:322px;top:957px;font-size:15px;line-height:17px;color:#333;list-style:none}
.charge-text{left:643px;top:960px;width:420px;font-size:14px;line-height:17px;color:#333}

.blue-rule{left:132px;top:1085px;width:924px;height:1px;background:var(--rule-blue)}
.second-title{left:533px;top:1117px;font-family:"Oswald",sans-serif;font-weight:600;font-size:37px;color:var(--accent-orange);letter-spacing:.5px}
.orange-rule{left:480px;top:1198px;width:480px;height:1px;background:var(--soft-orange)}

.bracket{width:30px;height:30px;border-color:var(--accent-orange);border-style:solid}
.card-image{left:240px;top:1279px;width:156px;height:161px;background:radial-gradient(circle at 50% 60%,#9a9a9a,#e6e6e6 70%,#fff)}
.card-title{left:386px;top:1260px;font-family:"Cinzel",serif;font-size:18px;color:var(--title-teal)}
.card-text{left:413px;top:1313px;width:642px;font-size:13px;line-height:15.5px;color:var(--body-grey)}
.read-more{left:984px;top:1437px;font-size:10px;font-weight:700;color:var(--accent-orange)}

.wide-rule{left:132px;top:1522px;width:996px;height:1px;background:var(--rule-grey)}
.wide-rule-mark{left:643px;top:1519px;width:87px;height:6px;background:var(--accent-orange)}
.activities-title{left:0;width:1368px;top:1560px;text-align:center;font-family:"Oswald",sans-serif;font-weight:600;font-size:37px;color:var(--ink)}

.contact-banner{left:211px;top:1656px;width:317px;height:53px;background:var(--banner-blue);color:#fff;font-size:26px;font-weight:700;padding:12px 0 0 30px}
.contact-fold{left:211px;top:1709px;width:0;height:0;border-top:12px solid #1d4c7a;border-left:14px solid transparent}
.contact-phone-box{left:528px;top:1656px;width:60px;height:53px;background:var(--accent-orange)}
.person{left:230px;top:1728px}
.small-text{font-size:13px;line-height:15.5px;color:var(--body-grey)}
.thin-rule{height:1px;background:var(--rule-grey)}
.phone-number{left:348px;top:1862px;font-size:14px;color:var(--accent-orange)}
.slider-title{left:259px;top:1934px;font-size:22px;font-weight:700;color:#4a5a75}

.channel-title{left:694px;top:1686px;font-size:20px;font-weight:700}
.video{left:686px;top:1766px;width:360px;height:226px}

.footer-col{top:2112px;font-size:11px}
.footer-head{font-size:11px;letter-spacing:.5px;margin-bottom:10px;color:#222}
.footer-links{list-style:none;font-size:9px;font-weight:700;line-height:20px;color:#222}
.footer-news{width:220px;font-size:10px;line-height:13px;color:#555}
.branch-row{display:flex;gap:10px;font-size:10px;line-height:13px;color:#555;margin-bottom:12px;width:240px}
.social-dot{width:28px;height:28px;border-radius:50%;background:#1e1e1e}
.copyright-rule{left:449px;width:343px;height:1px}
.copyright{left:0;width:1200px;top:2303px;text-align:center;font-size:10px;letter-spacing:2px;color:#333}
</style>
</head>
<body>

<header>
  <div class="abs top-rule"></div>
  <div class="abs top-divider" style="left:820px"></div>
  <div class="abs top-divider" style="left:975px"></div>
  <div class="abs top-tab"></div>

  <div class="abs logo">
    <div class="logo-name">PELBROOK</div>
    <div class="logo-tag">refurbishing equipment</div>
  </div>

  <nav class="abs main-nav" style="left:0">
    <svg class="abs" style="left:434px;top:-2px" width="22" height="20" viewBox="0 0 22 20" aria-hidden="true"><path d="M11 1 L21 10 H18 V19 H13 V13 H9 V19 H4 V10 H1 Z" fill="#d2571b"/></svg>
    <span class="current" style="left:473px">HOME</span>
    <span style="left:588px">ABOUT</span>
    <span style="left:703px">SERVICES</span>
    <span style="left:835px">SECTORS</span>
    <span style="left:950px">CONTACT US</span>
  </nav>
</header>

<main>
  <div class="abs hero-shadow"></div>
  <div class="abs hero" role="img" aria-label="Close-up photograph of a gloved hand holding a small blue-capped medical vial"></div>

  <section class="about">
    <div class="abs section-rule" style="left:492px;top:778px;width:377px"></div>
    <div class="abs icon-badge" style="left:408px;top:794px;width:48px;height:48px"></div>
    <svg class="abs" style="left:418px;top:806px" width="28" height="24" viewBox="0 0 28 24" aria-hidden="true"><path d="M14 3 L27 9 L14 15 L1 9 Z M6 12 V18 C6 20 22 20 22 18 V12 L14 16 Z" fill="#fff"/></svg>
    <h2 class="abs about-title">ABOUT MY HISTORY AND PRICES</h2>

    <h3 class="abs col-title" style="left:269px;top:893px;width:340px">MY CLIENTS ARE LOCATED EVERYWHERE</h3>
    <div class="abs map" role="img" aria-label="World map with client locations highlighted"></div>
    <ul class="abs client-list">
      <li>United States</li>
      <li>Manila (Philippines)</li>
      <li>Canada</li>
      <li>India</li>
    </ul>

    <div class="abs icon-badge" style="left:633px;top:883px;width:44px;height:44px;background:#4a4f58"></div>
    <div class="abs" style="left:633px;top:889px;width:44px;text-align:center;color:#fff;font-size:24px;font-weight:700">$</div>
    <h3 class="abs col-title" style="left:701px;top:898px">HOW MUCH DO I CHARGE?</h3>
    <p class="abs charge-text">I get the majority of my work through referrals, and I have references available at your request. The rest of my business comes from this short letter and its associated advertisement on Searchwell.</p>
  </section>

  <div class="abs blue-rule"></div>

  <section class="second">
    <svg class="abs" style="left:424px;top:1108px" width="64" height="64" viewBox="0 0 64 64" aria-hidden="true">
      <circle cx="32" cy="34" r="22" fill="none" stroke="#5d6a80" stroke-width="5"/>
      <path d="M32 22 V35 L40 40" fill="none" stroke="#5d6a80" stroke-width="4" stroke-linecap="round"/>
      <path d="M6 14 A10 10 0 0 1 20 6 Z M58 14 A10 10 0 0 0 44 6 Z" fill="#5d6a80"/>
      <path d="M16 54 L11 60 M48 54 L53 60" stroke="#5d6a80" stroke-width="4" stroke-linecap="round"/>
    </svg>
    <h2 class="abs second-title">SECOND SECTIONS</h2>
    <div class="abs orange-rule"></div>

    <div class="abs bracket" style="left:257px;top:1265px;border-width:3px 0 0 3px"></div>
    <div class="abs card-image" role="img" aria-label="Illustration of a hammer striking cracked ground"></div>
    <div class="abs bracket" style="left:371px;top:1415px;border-width:0 3px 3px 0;border-color:#222"></div>
    <h3 class="abs card-title">Predictive Auto Dialers</h3>
    <p class="abs card-text">Marlow is NOT directly affiliated with the Dialnova project. He is an independent support consultant for Dialnova (and voice services in general to some degree). More importantly he is a great person and quite possibly greatest consultant there is out there, anywhere.Marlow is NOT directly affiliated with the Dialnova project. He is an independent support consultant for Dialnova (and voice services in general to some degree). More importantly he is a great person and quite possibly greatest consultant there is out there, anywhere..</p>
    <div class="abs read-more">READ MORE</div>
  </section>

  <div class="abs wide-rule"></div>
  <div class="abs wide-rule-mark"></div>
  <h2 class="abs activities-title">ACTIVATIES</h2>

  <section class="contact">
    <div class="abs contact-banner">CONTACT US</div>
    <div class="abs contact-fold"></div>
    <div class="abs contact-phone-box"></div>
    <svg class="abs" style="left:544px;top:1668px" width="28" height="30" viewBox="0 0 28 30" aria-hidden="true"><path d="M6 2 L11 2 L13 9 L9 12 C11 17 13 20 17 22 L20 18 L27 20 L27 25 C27 28 24 29 20 28 C10 25 3 16 2 7 C2 4 3 2 6 2 Z" fill="#fff"/></svg>

    <svg class="abs person" width="82" height="96" viewBox="0 0 82 96" aria-hidden="true">
      <circle cx="41" cy="20" r="18" fill="#222"/>
      <path d="M4 94 V64 C4 50 16 42 28 42 H54 C66 42 78 50 78 64 V94 Z" fill="#222"/>
      <path d="M36 42 L41 62 L46 42 Z" fill="#fff"/>
    </svg>
    <p class="abs small-text" style="left:343px;top:1757px;width:245px">Dialnova (and voice services in general to some degree). More importantly he is a great person and quite possibly greate</p>
    <div class="abs thin-rule" style="left:343px;top:1829px;width:233px"></div>
    <div class="abs phone-number">00800 414 907 62</div>
    <svg class="abs" style="left:490px;top:1848px" width="34" height="38" viewBox="0 0 34 38" aria-hidden="true"><rect x="8" y="8" width="16" height="28" rx="2" fill="none" stroke="#222" stroke-width="2.5"/><rect x="11" y="12" width="10" height="16" fill="#222"/><rect x="2" y="1" width="16" height="9" rx="2" fill="#222"/></svg>
    <div class="abs thin-rule" style="left:259px;top:1913px;width:317px"></div>
    <h3 class="abs slider-title">NEW SLIDER</h3>
    <p class="abs small-text" style="left:259px;top:1982px;width:345px">Dialnova (and voice services in general to some degree). More importantly he is a great person and quite possibly greate</p>
    <div class="abs thin-rule" style="left:211px;top:2052px;width:377px"></div>
  </section>

  <section class="channel">
    <div class="abs thin-rule" style="left:679px;top:1651px;width:377px"></div>
    <h3 class="abs channel-title">STREAMORA CHANNEL</h3>
    <svg class="abs video" viewBox="0 0 360 226" aria-label="Video player">
      <rect x="0" y="0" width="360" height="226" rx="4" fill="#1a1a1a"/>
      <rect x="8" y="8" width="344" height="196" fill="#e9e9e9"/>
      <path d="M168 88 L196 106 L168 124 Z" fill="#111"/>
      <rect x="8" y="206" width="344" height="14" fill="#2a2a2a"/>
      <rect x="30" y="212" width="180" height="3" fill="#888"/>
      <circle cx="60" cy="213" r="4" fill="#ddd"/>
      <rect x="12" y="209" width="8" height="8" fill="#bbb"/>
      <rect x="300" y="209" width="40" height="8" fill="#777"/>
    </svg>
    <div class="abs thin-rule" style="left:679px;top:2052px;width:377px"></div>
  </section>
</main>

<footer>
  <div class="abs footer-col" style="left:228px">
    <div class="footer-head">HOME</div>
    <ul class="footer-links">
      <li>ABOUT</li>
      <li>SERVICES</li>
      <li>CONTACT US</li>
    </ul>
  </div>
  <div class="abs footer-col" style="left:379px">
    <div class="footer-head">HOT NEWS</div>
    <p class="footer-news">Sample news line goes here and serves to reserve space. More useful data will follow and serves to reserve space where real data is normally......</p>
  </div>
  <div class="abs footer-col" style="left:624px">
    <div class="footer-head">BRANCH</div>
    <div class="branch-row"><span style="display:inline-block;width:10px;height:10px;border-radius:50%;background:#222;margin-top:1px"></span><span>18 Kessel Strasse, Lindau</span></div>
    <div class="branch-row"><span style="display:inline-block;width:10px;height:10px;background:#222;margin-top:1px"></span><span>BRANCH: Harbor Road 42, Port Ellis</span></div>
  </div>
  <div class="abs footer-col" style="left:958px">
    <div class="footer-head">FOLLOW US</div>
  </div>
  <div class="abs social-dot" style="left:956px;top:2139px"></div>
  <div class="abs social-dot" style="left:990px;top:2139px"></div>
  <div class="abs social-dot" style="left:1025px;top:2139px"></div>

  <div class="abs copyright-rule" style="top:2292px;background:#333"></div>
  <div class="abs copyright">ALL COPYRIGHTS RESERVED BY YOURCOMPANY</div>
  <div class="abs copyright-rule" style="top:2328px;background:var(--soft-orange)"></div>
</footer>

</body>
</html>
```